Brightoak Billboard

Please design a billboard using my photos and logos.
For photo of truck please crop the truck itself out and not have the trees / dirt in photo.
Please put " Best Prices in Sevier County"
Please put " 30-yard Dumpsters Starting at 600.00"
Please put " 16-yard Dumpsters Starting at 300.0"
Please put " Delivery and Pickup 7 Days a week"
Billboard size will be 10 ft tall 30 ft wide

```html
<!DOCTYPE html>
<html lang="en">
<head>
<meta charset="utf-8">
<title>Brightoak Billboard</title>
<link rel="stylesheet" href="https://fonts.googleapis.com/css2?family=Montserrat:wght@600;700;800&display=swap">
<style>
  :root {
    --page: #eef0f3;
    --board: #1c1c1e;
    --purple: #9656b5;
    --purple-deep: #7d3f9c;
    --white: #ffffff;
    --stripe-grey: #3a3a3c;
    --truck-light: #e9ebee;
    --truck-mid: #b9bec4;
  }
  html, body {
    margin: 0;
    width: 1200px;
    height: 1200px;
    overflow: hidden;
    background: var(--page);
    font-family: "Montserrat", Arial, sans-serif;
  }
  .billboard {
    position: absolute;
    left: 20px;
    top: 310px;
    width: 1160px;
    height: 580px;
    background: var(--board);
    overflow: hidden;
  }
  .billboard-shapes {
    position: absolute;
    inset: 0;
  }
  .brand-name {
    position: absolute;
    left: 70px;
    top: 36px;
    margin: 0;
    color: var(--white);
    font-weight: 800;
    font-size: 72px;
    line-height: 0.95;
    letter-spacing: 1px;
    text-transform: uppercase;
  }
  .brand-name .brand-sub {
    display: block;
    font-size: 40px;
    padding-left: 150px;
  }
  .tagline-band {
    position: absolute;
    left: 0;
    top: 200px;
    width: 640px;
    height: 44px;
    background: var(--purple);
  }
  .tagline {
    position: absolute;
    left: 70px;
    top: 209px;
    margin: 0;
    color: var(--white);
    font-weight: 700;
    font-size: 22px;
    letter-spacing: 0.5px;
    text-transform: uppercase;
  }
  .offer {
    position: absolute;
    left: 70px;
    margin: 0;
  }
  .offer-30 { top: 262px; }
  .offer-16 { top: 360px; }
  .offer-label {
    display: block;
    color: var(--white);
    font-weight: 600;
    font-size: 18px;
    letter-spacing: 0.5px;
    text-transform: uppercase;
  }
  .offer-price {
    display: block;
    color: var(--purple);
    font-weight: 800;
    font-size: 72px;
    line-height: 1;
  }
  .service-band {
    position: absolute;
    left: 0;
    top: 462px;
    width: 700px;
    height: 100px;
    background: var(--purple);
    clip-path: polygon(0 0, 100% 0, 92% 100%, 0 100%);
  }
  .service {
    position: absolute;
    left: 70px;
    top: 470px;
    margin: 0;
    text-transform: uppercase;
    color: var(--board);
  }
  .service-label {
    display: block;
    font-weight: 700;
    font-size: 24px;
  }
  .service-days {
    display: block;
    color: var(--white);
    font-weight: 800;
    font-size: 44px;
    line-height: 1.05;
  }
  .truck-photo {
    position: absolute;
    left: 480px;
    top: 150px;
    width: 640px;
    height: 400px;
    border-radius: 30px 30px 10px 10px;
    background: linear-gradient(160deg, var(--truck-light) 0%, var(--truck-mid) 70%, #4a4a52 100%);
  }
</style>
</head>
<body>
  <main class="billboard">
    <svg class="billboard-shapes" viewBox="0 0 1160 580" width="1160" height="580" aria-hidden="true">
      <polygon points="820,80 870,80 700,580 650,580" fill="var(--white)"/>
      <polygon points="870,80 900,80 730,580 700,580" fill="var(--stripe-grey)"/>
      <polygon points="900,80 1160,80 1160,580 730,580" fill="var(--purple)"/>
    </svg>

    <h1 class="brand-name">Brightoak<span class="brand-sub">Dumpsters</span></h1>

    <div class="tagline-band"></div>
    <p class="tagline">Best Prices in Sevier County</p>

    <p class="offer offer-30">
      <span class="offer-label">30-Yard Dumpsters Starting At</span>
      <span class="offer-price">600.00</span>
    </p>
    <p class="offer offer-16">
      <span class="offer-label">16-Yard Dumpsters Starting At</span>
      <span class="offer-price">300.00</span>
    </p>

    <div class="service-band"></div>
    <p class="service">
      <span class="service-label">Delivery and Pickup</span>
      <span class="service-days">7 Days a Week</span>
    </p>

    <div class="truck-photo" role="img" aria-label="Photo of a white roll-off dumpster truck, cut out from its background"></div>
  </main>
</body>
</html>
```